We need a tri-fold brochure for our business called: KindlePath. (KindlePath Therapy Services)
This is a therapy services business that offers Physiotherapy and Occupational Therapy to children aged 5 to 16 years of age. The focus is on Neuro-developmental therapy and the children have a range of conditions such as Cerebral-Palsy, brain injuries etc... We are looking for designs that focus on children, fun and the word nurture.
Target Market(s)
Primarily parents and people looking for therapy services.
Industry/Entity Type
Business
Font styles to use
Sans Serif

```html
<!DOCTYPE html>
<html lang="en">
<head>
<meta charset="utf-8">
<title>KindlePath Therapy Services – Tri-fold Brochure</title>
<link rel="stylesheet" href="https://fonts.googleapis.com/css2?family=Exo+2:wght@400;500;600;700&display=swap">
<style>
  :root {
    --teal-dark: #0c5f5a;
    --teal: #14968c;
    --teal-mid: #1fa89b;
    --teal-light: #6fd3c6;
    --paper: #f3f4f4;
    --grey-light: #dcdede;
    --grey: #9a9d9f;
    --grey-dark: #7c7f82;
    --white: #ffffff;
    --ink-teal: #0e6a62;
    --backdrop: #e9ecec;
  }
  * { box-sizing: border-box; margin: 0; padding: 0; }
  html, body { width: 1200px; height: 1000px; overflow: hidden; }
  body {
    background: var(--backdrop);
    font-family: "Exo 2", "Trebuchet MS", sans-serif;
    display: flex; align-items: center; justify-content: center;
  }
  .brochure {
    display: flex; width: 1140px; height: 900px;
    box-shadow: 0 8px 30px rgba(0,0,0,.18);
  }
  .panel {
    position: relative; width: 380px; height: 900px; overflow: hidden;
    background: linear-gradient(180deg, var(--teal) 0%, var(--teal-mid) 45%, var(--teal-light) 55%, var(--paper) 64%, var(--paper) 100%);
    border-right: 1px solid rgba(0,0,0,.08);
  }
  .panel:last-child { border-right: none; }
  .panel-header {
    position: absolute; top: 0; left: 0; right: 0; height: 190px;
    background: var(--teal-dark);
    display: flex; flex-direction: column; align-items: center; justify-content: center;
    color: var(--white); text-align: center;
    border-bottom: 4px solid var(--teal-light);
  }
  .panel-footer {
    position: absolute; left: 0; right: 0; bottom: 0; height: 120px;
    background: var(--grey);
  }
  .panel-footer::before {
    content: ""; position: absolute; left: 0; right: 0; top: -40px; height: 40px;
    background: linear-gradient(170deg, transparent 49%, var(--grey-light) 50%);
  }

  /* Panel 1 */
  .get-started-title { font-size: 40px; font-weight: 700; line-height: 1.15; letter-spacing: .5px; }
  .get-started-copy {
    position: absolute; top: 240px; left: 40px; right: 34px;
    color: var(--white); font-size: 18px; font-weight: 600; line-height: 1.32; text-align: right;
    text-shadow: 0 1px 2px rgba(0,0,0,.25);
  }

  /* Panel 2 */
  .schedule-title { font-size: 26px; font-weight: 600; line-height: 1.2; }
  .schedule-phone { margin-top: 12px; font-size: 20px; font-weight: 500; letter-spacing: 1px; }
  .photo-grid {
    position: absolute; top: 235px; left: 36px; right: 36px;
    display: grid; grid-template-columns: 1fr 1fr; gap: 26px 30px;
  }
  .photo-tile { height: 120px; border-radius: 26px 6px 26px 6px; border: 3px solid var(--white); }
  .photo-tile.t1 { background: linear-gradient(135deg, #7a6a9e, #c9b9d8); }
  .photo-tile.t2 { background: linear-gradient(135deg, #8a6a55, #e2cbb4); }
  .photo-tile.t3 { background: linear-gradient(135deg, #d14a3c, #e9d6cf); }
  .photo-tile.t4 { background: linear-gradient(135deg, #4e8a3a, #a9c98a); }
  .hours {
    position: absolute; top: 570px; left: 0; right: 0; text-align: center; color: var(--ink-teal);
  }
  .hours-title { font-size: 26px; font-weight: 700; line-height: 1.15; }
  .hours-days { margin-top: 18px; font-size: 17px; font-weight: 700; }
  .hours-time { margin-top: 24px; font-size: 17px; font-weight: 700; }
  .contact-lines {
    position: absolute; bottom: 22px; left: 0; right: 0; text-align: center;
    color: var(--white); font-size: 11px; line-height: 1.7; letter-spacing: .3px; z-index: 1;
  }

  /* Panel 3 */
  .brand { display: flex; align-items: center; gap: 14px; }
  .brand-dot { width: 30px; height: 30px; border-radius: 50%; background: var(--teal-light); }
  .brand-name { font-size: 40px; font-weight: 600; color: var(--white); }
  .label-bar {
    position: absolute; height: 44px; background: var(--teal-dark);
    color: var(--white); font-size: 20px; font-weight: 500;
    display: flex; align-items: center; padding: 0 22px;
  }
  .label-bar.name { top: 205px; left: 10px; width: 210px; }
  .label-bar.services { top: 258px; right: 0; width: 220px; }
  .cover-photo { position: absolute; top: 318px; left: 0; width: 380px; height: 250px; }

  .handprints {
    position: absolute; top: 640px; left: 100px; width: 180px; height: 110px; border-radius: 40px;
    background: linear-gradient(100deg, #39b4e6 0%, #e8489a 35%, #f2c53a 65%, #7cc242 100%);
    opacity: .8;
  }
  .social-row {
    position: absolute; bottom: 62px; left: 0; right: 0; display: flex; justify-content: center; gap: 14px; z-index: 1;
  }
  .social-dot { width: 26px; height: 26px; border-radius: 50%; background: var(--white); border: 2px solid var(--grey-light); }
</style>
</head>
<body>
  <main class="brochure">

    <section class="panel panel-get-started">
      <header class="panel-header">
        <h2 class="get-started-title">HOW TO<br>GET STARTED</h2>
      </header>
      <p class="get-started-copy">Lorem ipsum dolor sit amet, consectetuer adipiscing elit, sed diam nonummy nibh euismod tincidunt ut laoreet dolore magna aliquam erat volutpat. Ut wisi enim ad minim veniam, quis nostrud exerci tation ullamcorper suscipit lobortis nisl ut aliquip ex ea commodo consequat. Duis autem vel eum iriure dolor in</p>
      <div class="handprints" role="img" aria-label="Colourful painted children's handprints"></div>
      <div class="panel-footer"></div>
    </section>

    <section class="panel panel-schedule">
      <header class="panel-header">
        <h2 class="schedule-title">TO SCHEDULE<br>AN APPOINTMENT, CALL</h2>
        <p class="schedule-phone">0400-555-0123</p>
      </header>
      <div class="photo-grid">
        <div class="photo-tile t1" role="img" aria-label="Therapist working with a child on a play mat"></div>
        <div class="photo-tile t2" role="img" aria-label="Smiling toddler during a therapy session"></div>
        <div class="photo-tile t3" role="img" aria-label="Child balancing on a red therapy ball with a therapist"></div>
        <div class="photo-tile t4" role="img" aria-label="Child using a walker outdoors on grass"></div>
      </div>
      <div class="hours">
        <h3 class="hours-title">BUSSINESS<br>HOURS</h3>
        <p class="hours-days">MONDAY-SATURDAY</p>
        <p class="hours-time">6AM-7PM</p>
      </div>
      <div class="panel-footer"></div>
      <address class="contact-lines">
        HELLO@KINDLEPATH.EXAMPLE<br>
        Dana L. Reyes, 418 Willow Lane, Maple Grove, OR 97000<br>
        0400-555-0188
      </address>
    </section>

    <section class="panel panel-cover">
      <header class="panel-header">
        <div class="brand">
          <span class="brand-dot"></span>
          <span class="brand-name">KindlePath</span>
        </div>
      </header>
      <div class="label-bar name">KindlePath</div>
      <div class="label-bar services">Therapy Services</div>
      <svg class="cover-photo" viewBox="0 0 380 250" role="img" aria-label="Happy young boy seated in a supportive wheelchair in a bright classroom">
        <defs>
          <linearGradient id="coverPhotoTone" x1="0" y1="0" x2="1" y2="1">
            <stop offset="0" stop-color="#e6dccd"/>
            <stop offset="0.5" stop-color="#c9b9a0"/>
            <stop offset="1" stop-color="#5c7d5a"/>
          </linearGradient>
        </defs>
        <path d="M0 0 H380 V250 L60 215 Q10 205 0 160 Z" fill="url(#coverPhotoTone)"/>
        <path d="M0 160 Q10 205 60 215 L380 250" fill="none" stroke="#14968c" stroke-width="4"/>
      </svg>
      <div class="handprints" role="img" aria-label="Colourful painted children's handprints"></div>
      <div class="panel-footer"></div>
      <div class="social-row">
        <span class="social-dot"></span>
        <span class="social-dot"></span>
        <span class="social-dot"></span>
        <span class="social-dot"></span>
      </div>
    </section>

  </main>
</body>
</html>
```